Redesign Of Flower Delivery Subscription Service Website

I need a revamped website of www.petal-rush.com

Please revamp current design using same content....

Target Market(s)

people who buy flowers. Brides, wedding planners, wedding photographer, married man, boyfriend, etc.

Industry/Entity Type

Florist

Number of Pages Required

5+ page

Colors

Designer to choose colors to be used in the design.

Requirements
Must have
• I need a revamped website of www.petal-rush.com
• Please revamp current design using same content....
Nice to have
Should not have

```html
<!DOCTYPE html>
<html lang="en">
<head>
<meta charset="utf-8">
<title>Petal Rush – Buy now</title>
<link href="https://fonts.googleapis.com/css2?family=Montserrat:wght@300;400;500;600;700&family=Great+Vibes&display=swap" rel="stylesheet">
<style>
:root{
  --green:#8fd14f;
  --green-dark:#6cb52e;
  --ink:#333640;
  --muted:#8a8d96;
  --soft:#f7f8fc;
  --field:#f4f5fa;
  --line:#d9dbe2;
  --white:#ffffff;
}
*{box-sizing:border-box;margin:0;padding:0}
html,body{width:676px;height:1200px;overflow:hidden;background:var(--white)}
body{font-family:'Montserrat',sans-serif;color:var(--ink);position:relative}
.abs{position:absolute}
.site-header{left:0;top:0;width:676px;height:58px;border-bottom:1px solid var(--line)}
.call{left:90px;top:27px;font-size:5.6px;color:var(--muted);display:flex;align-items:center;gap:5px}
.call b{color:var(--ink);font-weight:600}
.flourish{top:18px;width:42px;height:24px;background:linear-gradient(90deg,rgba(80,80,80,0),rgba(80,80,80,.18));border-radius:12px}
.brand{left:298px;top:22px;width:80px;text-align:center;font-size:11px;font-weight:400;letter-spacing:.5px;color:var(--ink)}
.search{left:511px;top:28px}
.buy-btn{left:531px;top:22px;width:55px;height:17px;border-radius:9px;background:var(--white);box-shadow:0 2px 6px rgba(0,0,0,.08);font-size:5.4px;font-weight:600;color:var(--green);display:flex;align-items:center;justify-content:center;gap:3px}
.main-nav{left:0;top:59px;width:676px;height:28px;font-size:5.6px;color:var(--muted)}
.main-nav span{position:absolute;top:11px}
.hero{left:0;top:87px;width:676px;height:131px;background:var(--soft)}
.hero-left{left:0;top:123px;width:119px;height:95px;background:radial-gradient(circle at 80% 55%,#e9a825 0 18%,rgba(233,168,37,0) 19%),linear-gradient(35deg,#e6d7e4,#f3eef2 60%,rgba(247,248,252,0));border-radius:0 60px 0 0}
.hero-right{left:582px;top:87px;width:94px;height:99px;background:radial-gradient(circle at 60% 30%,#f1eee4 0 22%,rgba(0,0,0,0) 23%),linear-gradient(200deg,#3f5a3d,#6f8a64 55%,rgba(247,248,252,0));border-radius:0 0 0 60px}
.hero-title{left:0;top:134px;width:676px;text-align:center;font-family:'Great Vibes',cursive;font-size:22px;color:var(--green)}
.crumb{left:0;top:163px;width:676px;text-align:center;font-size:7px;color:var(--ink)}
.order-card{left:188px;top:235px;width:300px;height:757px;background:var(--white);box-shadow:0 2px 14px rgba(40,50,80,.08)}
.section-title{left:188px;width:300px;text-align:center;font-size:9px;font-weight:400}
.divider{left:188px;width:300px;height:1px;background:var(--green)}
.opt{font-size:7px;display:flex;align-items:center;gap:7px}
.radio{width:7px;height:7px;border:1px solid var(--green);border-radius:50%;display:inline-block;flex:none}
.radio.on{background:var(--green)}
.desc{left:206px;width:265px;font-size:5.1px;line-height:8.4px;color:var(--muted)}
.field{background:var(--field);height:14px;font-size:6.3px;color:var(--muted);padding-left:7px;display:flex;align-items:center}
.field.filled{color:var(--ink)}
.caret{position:absolute;right:5px;top:3px;width:8px;height:8px;border:1px solid var(--green);border-radius:1px;display:flex;align-items:center;justify-content:center}
.q{font-size:5.9px;color:var(--ink)}
.verify{left:188px;top:840px;width:300px;text-align:center;font-size:8.6px;font-weight:700;letter-spacing:.1px}
.verify-text{left:210px;top:865px;width:256px;text-align:center;font-size:5.2px;line-height:10.6px}
.row-label{left:206px;font-size:6.8px}
.send{left:187px;top:1004px;width:301px;height:14px;border-radius:7px;background:var(--green);color:var(--white);font-size:6.4px;font-weight:700;display:flex;align-items:center;justify-content:center}
.site-footer{left:0;top:1046px;width:676px;height:154px;background:var(--soft)}
.foot-brand{left:90px;top:1073px;font-size:11px;letter-spacing:.5px;color:var(--ink)}
.upgrade{left:94px;top:1104px;font-size:6px;font-weight:600;display:flex;align-items:center;gap:7px}
.email{left:90px;top:1123px;width:91px;height:15px;background:#ebecf1;font-size:5.2px;color:var(--ink);padding-left:6px;display:flex;align-items:center}
.submit{left:181px;top:1123px;width:32px;height:15px;background:var(--green);color:var(--white);font-size:5.2px;display:flex;align-items:center;justify-content:center}
.foot-head{top:1071px;font-size:6px;font-weight:600}
.foot-list{font-size:4.5px;color:var(--ink);line-height:10.6px}
.contact-item{left:465px;font-size:4.5px;display:flex;align-items:center;gap:4px}
.social{top:1120px;width:6px;height:6px;border-radius:50%;background:#9a9ca4}
.foot-rule{left:90px;top:1155px;width:496px;height:1px;background:#e6e7ec}
.copy{left:0;top:1174px;width:676px;text-align:center;font-size:5.2px}
.legal{left:486px;top:1174px;width:100px;text-align:right;font-size:5.2px}
</style>
</head>
<body>

<header class="abs site-header">
  <div class="abs call">
    <svg width="7" height="8" viewBox="0 0 7 8"><rect x="1" y=".5" width="5" height="7" rx="1" fill="none" stroke="#8fd14f" stroke-width=".8"/><line x1="2.5" y1="6" x2="4.5" y2="6" stroke="#8fd14f" stroke-width=".6"/></svg>
    Call now: <b>555-210-4477</b>
  </div>
  <div class="abs flourish" style="left:240px" role="img" aria-label="Decorative flourish"></div>
  <div class="abs brand">PETAL RUSH</div>
  <div class="abs flourish" style="left:395px;transform:scaleX(-1)" role="img" aria-label="Decorative flourish"></div>
  <svg class="abs search" width="8" height="8" viewBox="0 0 8 8"><circle cx="3.4" cy="3.4" r="2.7" fill="none" stroke="#8a8d96" stroke-width=".7"/><line x1="5.4" y1="5.4" x2="7.6" y2="7.6" stroke="#8a8d96" stroke-width=".7"/></svg>
  <div class="abs buy-btn">
    <svg width="5" height="6" viewBox="0 0 5 6"><rect x=".4" y="2.2" width="4.2" height="3.4" fill="none" stroke="#8fd14f" stroke-width=".6"/><path d="M1.3 2.2V1.4a1.2 1.2 0 0 1 2.4 0v.8" fill="none" stroke="#8fd14f" stroke-width=".6"/></svg>
    Buy now
  </div>
</header>

<nav class="abs main-nav">
  <span style="left:91px">Home</span>
  <span style="left:132px">How it works</span>
  <span style="left:189px">Delivry areas</span>
  <span style="left:249px">Franchise</span>
  <span style="left:300px">Blog</span>
  <span style="left:337px">Free flowers monthly</span>
  <span style="left:418px">Corporate Arrangements</span>
  <span style="left:508px">Help</span>
  <span style="left:544px;top:9px"><svg width="7" height="8" viewBox="0 0 7 8"><circle cx="3.5" cy="2.4" r="1.8" fill="none" stroke="#8a8d96" stroke-width=".6"/><path d="M.5 7.6c0-2 1.4-3 3-3s3 1 3 3z" fill="none" stroke="#8a8d96" stroke-width=".6"/></svg></span>
  <span style="left:554px">My account</span>
</nav>

<section class="abs hero">
</section>
<div class="abs hero-left" role="img" aria-label="Orchid sprigs and a yellow ranunculus"></div>
<div class="abs hero-right" role="img" aria-label="Bouquet of white and pink roses with fern leaves"></div>
<h1 class="abs hero-title">Buy now</h1>
<div class="abs crumb">Home / Buy now</div>

<main class="abs order-card"></main>

<h2 class="abs section-title" style="top:257px">Choose delivery frequency</h2>
<div class="abs opt" style="left:205px;top:286px"><span class="radio"></span>Weekly</div>
<div class="abs opt" style="left:278px;top:286px"><span class="radio on"></span>Bi - Weekly</div>
<div class="abs opt" style="left:355px;top:286px"><span class="radio"></span>Monthly</div>
<div class="abs opt" style="left:418px;top:286px"><span class="radio"></span>Bi - Monthly</div>
<div class="abs opt" style="left:205px;top:314px"><span class="radio"></span>4 Special Dates only (Valentines Day, Mother's Day, Birthday and Anniversary)</div>
<div class="abs divider" style="top:349px"></div>

<h2 class="abs section-title" style="top:374px">Choose your flower arrangements</h2>
<div class="abs opt" style="left:205px;top:399px"><span class="radio"></span>Best value &amp; Free upgrate</div>
<p class="abs desc" style="top:413px">$69.95/mth = 12-18 Beautiful Premium Roses In A Vase, Hand Delivered. This Price Includes Tax, Free Delivery and Free Vase ($100 Value Every Month) Colors Of Roses &amp; Fillers Will Vary Depending On Season.</p>
<div class="abs opt" style="left:205px;top:445px"><span class="radio"></span>Great Value - Seasonal Flower Arrangement</div>
<p class="abs desc" style="top:459px">$69.95 = a beautiful seasonal flower arrangement in a vase, hand delivered monthly. (An $89 Value Every Month) Colors and types of flowers will vary depending on season.</p>
<div class="abs divider" style="top:495px"></div>

<h2 class="abs section-title" style="top:514px">Enter Recipient Information</h2>
<div class="abs field filled" style="left:206px;top:536px;width:264px">Wife<span class="caret"><svg width="4" height="3" viewBox="0 0 4 3"><path d="M.5.7 2 2.2 3.5.7" fill="none" stroke="#8fd14f" stroke-width=".6"/></svg></span></div>
<div class="abs field filled" style="left:206px;top:558px;width:127px">First name</div>
<div class="abs field filled" style="left:343px;top:558px;width:127px">Last name</div>

<div class="abs q" style="left:205px;top:584px">Is recipient a Male or a Female? (choose one)</div>
<div class="abs opt" style="left:338px;top:584px"><span class="radio"></span>Male</div>
<div class="abs opt" style="left:375px;top:584px"><span class="radio"></span>Female</div>
<div class="abs q" style="left:206px;top:600px">Are we delivering to Residence or Business. (choose one)</div>
<div class="abs opt" style="left:372px;top:600px"><span class="radio"></span>Business</div>
<div class="abs opt" style="left:423px;top:600px"><span class="radio"></span>Residence</div>

<div class="abs field" style="left:206px;top:617px;width:264px">Delivery address 1</div>
<div class="abs field" style="left:206px;top:638px;width:264px">Delivery address 2</div>
<div class="abs field" style="left:206px;top:660px;width:264px">City</div>
<div class="abs field" style="left:206px;top:681px;width:264px">California</div>
<div class="abs field" style="left:206px;top:704px;width:264px">Zip</div>
<div class="abs field" style="left:206px;top:727px;width:264px">Phone</div>
<div class="abs field" style="left:206px;top:750px;width:264px;height:49px;align-items:flex-start;padding-top:5px">Special delivery instructions</div>
<div class="abs divider" style="top:824px"></div>

<h2 class="abs verify">VERIFY SPECIAL DELIVERY DATES</h2>
<p class="abs verify-text">PetalRush allows you to specify special dates such as an Anniversary, Recipients Birthday, Mothers/Fathers Day &amp; Valentines Day. Simply answer the 4 questions below and Petal Rush will make your flower delivery on that specific day that month. Never forget these special days again!</p>

<div class="abs row-label" style="top:909px">What is Your Anniversary Date?</div>
<div class="abs field" style="left:328px;top:906px;width:67px;padding-left:5px">January<span class="caret"><svg width="4" height="3" viewBox="0 0 4 3"><path d="M.5.7 2 2.2 3.5.7" fill="none" stroke="#8fd14f" stroke-width=".6"/></svg></span></div>
<div class="abs field" style="left:402px;top:906px;width:68px;padding-left:5px">1<span class="caret"><svg width="4" height="3" viewBox="0 0 4 3"><path d="M.5.7 2 2.2 3.5.7" fill="none" stroke="#8fd14f" stroke-width=".6"/></svg></span></div>

<div class="abs row-label" style="top:931px">Is Recipient Parent?</div>
<div class="abs opt" style="left:282px;top:931px"><span class="radio"></span>Yes</div>
<div class="abs opt" style="left:315px;top:931px"><span class="radio"></span>No</div>

<div class="abs row-label" style="top:951px">Birthday of Recipient</div>
<div class="abs field" style="left:328px;top:948px;width:67px;padding-left:5px">January<span class="caret"><svg width="4" height="3" viewBox="0 0 4 3"><path d="M.5.7 2 2.2 3.5.7" fill="none" stroke="#8fd14f" stroke-width=".6"/></svg></span></div>
<div class="abs field" style="left:402px;top:948px;width:68px;padding-left:5px">1<span class="caret"><svg width="4" height="3" viewBox="0 0 4 3"><path d="M.5.7 2 2.2 3.5.7" fill="none" stroke="#8fd14f" stroke-width=".6"/></svg></span></div>

<div class="abs row-label" style="top:971px">Deliver Flowers On Valentine Day?</div>
<div class="abs opt" style="left:323px;top:971px"><span class="radio"></span>Yes</div>
<div class="abs opt" style="left:356px;top:971px"><span class="radio"></span>No</div>

<div class="abs send">SENT</div>

<footer class="abs site-footer"></footer>
<div class="abs foot-brand">PETAL RUSH</div>
<div class="abs upgrade">
  <svg width="10" height="9" viewBox="0 0 10 9"><rect x=".5" y="2.5" width="9" height="6" fill="none" stroke="#333640" stroke-width=".7"/><path d="M.5 2.5 5 6l4.5-3.5" fill="none" stroke="#333640" stroke-width=".7"/><path d="M5 0v3" stroke="#333640" stroke-width=".7"/></svg>
  Receive A Free Upgrade
</div>
<div class="abs email">Your email address</div>
<div class="abs submit">Submit</div>

<div class="abs foot-head" style="left:301px">More Services</div>
<ul class="abs foot-list" style="left:301px;top:1086px;list-style:none">
  <li>- Corporate Arrangements</li>
  <li>- Hotel Arrangements</li>
  <li>- Events</li>
  <li>- Weddings</li>
</ul>

<div class="abs foot-head" style="left:466px">Contact</div>
<div class="abs contact-item" style="top:1087px"><svg width="6" height="6" viewBox="0 0 6 6"><rect x="1" y=".3" width="4" height="5.4" rx=".7" fill="none" stroke="#8a8d96" stroke-width=".5"/></svg>555-210-4477</div>
<div class="abs contact-item" style="top:1097px"><svg width="6" height="6" viewBox="0 0 6 6"><rect x=".3" y="1" width="5.4" height="4" fill="none" stroke="#8a8d96" stroke-width=".5"/><path d="M.3 1 3 3.3 5.7 1" fill="none" stroke="#8a8d96" stroke-width=".5"/></svg>Email: support@petal-rush.com</div>
<div class="abs contact-item" style="top:1107px"><svg width="6" height="6" viewBox="0 0 6 6"><path d="M3 5.7S1 3.6 1 2.3a2 2 0 0 1 4 0C5 3.6 3 5.7 3 5.7z" fill="none" stroke="#8a8d96" stroke-width=".5"/></svg>1840 Orchard Lane, Brookfield CA 90000</div>
<span class="abs social" style="left:476px"></span>
<span class="abs social" style="left:487px"></span>
<span class="abs social" style="left:499px"></span>

<div class="abs foot-rule"></div>
<div class="abs copy">Petal Rush - Monthly Flowers Delivery Copyright 2018. All Rights Reserved.</div>
<div class="abs legal">Privacy Policy Terms &amp; Conditions</div>

</body>
</html>
```